Cover for a recovery from breast augmentation surgery pamphlet

Need a cover which includes my logo for new pamphlet on recovering from breast augmentation surgery It is just a quick how to guide.
I would like the cover to incorporate the PeLu logo(2 options given) and be simple and clean. Will require in a vector file as well.

The title:
Healing Gently, Step by Step...
AND THEN?!

By: PeLu

A little about me: I am an adult industry writer and am looking to do a mainstream project. This is a project I want to appeal to mainstream women.

Target Market(s)

Women who are recovering from or entertaining breast augmentation surgery

Font styles to use
Serif

Requirements
Must have
• One PeLu logo, titile, and by PeLu
Nice to have
• i love modern clean sleek design that is easy to read
Should not have
• nothing that would offend women or make them uncomfortable about their body

```html
<!DOCTYPE html>
<html lang="en">
<head>
<meta charset="utf-8">
<title>PeLu – Recovery Pamphlet Cover</title>
<link href="https://fonts.googleapis.com/css2?family=Cormorant+Garamond:wght@500;600&family=Open+Sans:wght@400&display=swap" rel="stylesheet">
<style>
  :root {
    --backdrop: #8e8c8d;
    --paper: #ffffff;
    --magenta: #c0308a;
    --magenta-deep: #a8267a;
    --magenta-soft: #e07cb8;
    --skin-light: #e7c2a8;
    --skin-mid: #d3a386;
    --logo-pale: #e9e4ea;
  }
  * { margin: 0; padding: 0; box-sizing: border-box; }
  html, body { width: 1200px; height: 1167px; overflow: hidden; }
  body {
    background: radial-gradient(ellipse at 50% 35%, #a9a7a8 0%, var(--backdrop) 75%);
    position: relative;
  }
  .cover {
    position: absolute;
    left: 210px; top: 32px;
    width: 780px; height: 1104px;
    background: var(--paper);
    overflow: hidden;
    box-shadow: 0 18px 40px rgba(0,0,0,.35);
  }
  .cover-art { position: absolute; inset: 0; }
  .brand {
    position: absolute;
    font-family: "Cormorant Garamond", serif;
    font-weight: 600;
    color: var(--magenta);
    line-height: 1;
  }
  .brand--top { right: 60px; top: 70px; font-size: 96px; }
  .brand--bottom { left: 70px; top: 940px; font-size: 78px; color: var(--logo-pale); }
  .title {
    position: absolute;
    left: 430px; top: 340px;
    width: 330px;
    text-align: center;
    font-family: "Cormorant Garamond", serif;
    font-weight: 500;
    color: var(--magenta);
    line-height: 1;
  }
  .title__lead { display: block; font-size: 40px; }
  .title__main { display: block; font-size: 48px; margin-top: 10px; letter-spacing: .5px; }
  .title__question { display: block; font-size: 92px; margin-top: 18px; line-height: .92; letter-spacing: 1px; }
  .divider {
    position: absolute;
    left: 250px; top: 920px;
    width: 1px; height: 130px;
    background: rgba(255,255,255,.55);
  }
  .intro {
    position: absolute;
    left: 272px; top: 922px;
    width: 470px;
    font-family: "Open Sans", sans-serif;
    font-size: 11.5px;
    line-height: 1.75;
    color: #fff;
  }
</style>
</head>
<body>
  <main class="cover">
    <svg class="cover-art" viewBox="0 0 780 1104" width="780" height="1104">
      <defs>
        <linearGradient id="skin" x1="0" y1="0" x2="1" y2="1">
          <stop offset="0" stop-color="var(--skin-light)"/>
          <stop offset="1" stop-color="var(--skin-mid)"/>
        </linearGradient>
        <linearGradient id="band" x1="0" y1="0" x2="1" y2="0">
          <stop offset="0" stop-color="var(--magenta-deep)"/>
          <stop offset=".6" stop-color="var(--magenta)"/>
          <stop offset="1" stop-color="var(--magenta-deep)"/>
        </linearGradient>
      </defs>
      <path role="img" aria-label="Photo of a woman's bare torso in profile, arm raised, hand modestly covering her chest"
            fill="url(#skin)"
            d="M0 70 C20 30 60 10 110 0 L420 0 C400 140 375 280 400 380 C430 500 500 650 560 780 L560 900 L0 920 Z"/>
      <path fill="var(--magenta-soft)" opacity=".7"
            d="M0 860 C260 845 560 760 780 640 L780 700 C560 800 260 875 0 890 Z"/>
      <path fill="url(#band)"
            d="M0 880 C260 865 560 790 780 675 L780 1104 L0 1104 Z"/>
    </svg>

    <div class="brand brand--top">PeLu</div>

    <h1 class="title">
      <span class="title__lead">Healing Gently,</span>
      <span class="title__main">STEP BY STEP...</span>
      <span class="title__question">AND<br>THEN?!</span>
    </h1>

    <div class="brand brand--bottom">PeLu</div>
    <div class="divider"></div>
    <p class="intro">Health is wealth and after breast augmentation surgery is definitely a time when you need the healthiest food. Stock your cupboards, pantry, refrigerator, and freezer with healthy food and staples. Meal replacement bars and/or shakes with protein powder are great for days where you need to rest rather than prepare food. Never would you guess how difficult grocery shopping and food prep can be when you cannot move your arms or carry more than a gallon of milk. Small amounts of produce are manageable to shop and carry after about a week post-surgery.</p>
  </main>
</body>
</html>
```